WordPress Website Design Project

Technical & Functional Deliverables
WordPress CMS
Fully responsive design
Integrated WhatsApp chatbot
Custom article filtering system
SEO-friendly site structure & performance optimization
CMS user manual & training session
Updates

Need extra days to review

Industry/Entity Type

Industrial Safety and Compliance

Coding

Coded - Design and coding required

Number of Pages Required

5+ page

Font styles to use
Sans Serif

Colors
0054AA
0677BA
7BADD7
CADEEF
E8F1F8

```html
<!DOCTYPE html>
<html lang="en">
<head>
<meta charset="UTF-8">
<title>Orvessa – Industrial Safety &amp; Compliance</title>
<link href="https://fonts.googleapis.com/css2?family=Montserrat:wght@400;500;600;700&display=swap" rel="stylesheet">
<style>
:root{
  --brand:#0054AA;
  --brand-mid:#0677BA;
  --brand-soft:#7BADD7;
  --brand-pale:#CADEEF;
  --brand-mist:#E8F1F8;
  --ink:#1d1d1f;
  --muted:#5b5f66;
  --panel:#eef1f4;
  --footer:#191e2c;
  --footer-base:#161616;
  --white:#ffffff;
}
*{box-sizing:border-box;margin:0;padding:0}
html,body{width:1200px;height:3940px;overflow:hidden}
body{position:relative;font-family:"Montserrat",sans-serif;color:var(--ink);background:var(--white)}
.btn{position:absolute;background:var(--brand);color:var(--white);font-weight:600;font-size:13px;display:flex;align-items:center;justify-content:center;text-decoration:none}
.section-title{position:absolute;left:0;width:1200px;text-align:center;font-size:33px;font-weight:500;color:var(--ink)}

/* Hero */
.hero{position:absolute;left:0;top:0;width:1200px;height:751px;background:linear-gradient(180deg,#202a38 0%,#4a5d78 45%,#6f83a0 75%,#56677f 100%)}
.site-header{position:absolute;left:75px;top:23px;width:1050px;height:87px;background:var(--white);display:flex;align-items:center;padding:0 30px}
.brand{display:flex;align-items:center;gap:10px;font-weight:700;font-size:36px;color:#1f2a44;letter-spacing:1px}
.brand-square{width:44px;height:44px;background:var(--brand-soft)}
.nav{margin-left:auto;display:flex;align-items:center;gap:20px;font-size:12px;color:#333}
.nav .btn{position:static;width:146px;height:41px;margin-left:12px}
.hero-title{position:absolute;left:0;top:240px;width:1200px;text-align:center;font-size:57px;font-weight:500;line-height:60px;color:var(--white)}
.scroll-badge{position:absolute;left:551px;top:611px;width:98px;height:98px}

/* About */
.about-lead{position:absolute;left:250px;top:895px;width:700px;text-align:center;font-size:12px;line-height:19px;color:var(--muted)}
.value{position:absolute;width:300px}
.value h4{font-size:14px;font-weight:600;color:var(--ink);margin-bottom:2px}
.value p{font-size:11.5px;line-height:17px;color:var(--muted)}
.value.left{text-align:right}
.value-icon{position:absolute;width:46px;height:46px;background:var(--brand);display:flex;align-items:center;justify-content:center}
.core-mark{position:absolute;left:494px;top:994px;width:211px;height:217px;background:#5f97d0}

/* Solutions */
.solutions{position:absolute;left:0;top:1319px;width:1200px;height:646px;background:var(--panel)}
.card{position:absolute;top:108px;width:326px;height:408px;background:var(--white)}
.card-icon{position:absolute;left:22px;top:21px;width:66px;height:66px;background:var(--brand);display:flex;align-items:center;justify-content:center}
.card h3{position:absolute;left:22px;top:96px;width:220px;font-size:15.5px;font-weight:500;line-height:23px;color:var(--ink)}
.card-photo{position:absolute;left:10px;top:164px;width:306px;height:234px}

/* Work */
.work-slide{position:absolute;top:2136px;height:336px}
.work-caption{position:absolute;left:32px;bottom:26px;color:var(--white)}
.work-caption h3{font-size:20px;font-weight:400;margin-bottom:8px}
.work-caption p{font-size:11px;line-height:16px;width:480px}

/* People */
.person{position:absolute;top:2624px;width:240px;text-align:center}
.person-photo{width:240px;height:309px}
.person h4{margin-top:14px;font-size:17px;font-weight:500;color:var(--ink)}
.person p{margin-top:4px;font-size:11.5px;color:var(--muted)}

/* Partners */
.partner{position:absolute;top:3219px;width:200px;height:80px;border:1.5px solid #c9ccd2;display:flex;align-items:center;justify-content:center}
.partner span{display:block;width:90px;height:30px;background:var(--brand-pale)}

/* Footer */
.footer-main{position:absolute;left:0;top:3419px;width:1200px;height:300px;background:var(--footer)}
.footer-tagline{position:absolute;left:77px;top:92px;font-size:30px;font-weight:500;line-height:37px;color:var(--white)}
.footer-nav{position:absolute;right:75px;top:136px;display:flex;gap:18px;align-items:center;font-size:12px;font-weight:700;color:var(--white)}
.footer-base{position:absolute;left:0;top:3719px;width:1200px;height:221px;background:var(--footer-base);color:var(--white)}
.legal{position:absolute;left:73px;top:72px;display:flex;gap:20px;font-size:11.5px;font-weight:700}
.footer-brand{position:absolute;right:75px;top:42px;display:flex;align-items:center;gap:10px;font-size:38px;font-weight:700;letter-spacing:1px}
.footer-brand .brand-square{width:42px;height:42px;background:var(--white)}
.footer-company{position:absolute;right:75px;top:98px;font-size:10.5px}
.footer-rule{position:absolute;left:75px;top:151px;width:1050px;height:1px;background:#3a3a3a}
.social{position:absolute;left:77px;top:176px;font-size:12px;font-weight:700}
.copyright{position:absolute;left:0;top:177px;width:1200px;text-align:center;font-size:10.5px;font-weight:700}
</style>
</head>
<body>

<section class="hero" role="img" aria-label="Dense city skyline of high-rise towers under a cloudy sky, in cool blue-grey tones">
  <header class="site-header">
    <div class="brand"><span class="brand-square"></span>ORVESSA</div>
    <nav class="nav">
      <span>About Us</span><span>|</span>
      <span>Solutions</span><span>|</span>
      <span>Articles</span>
      <span class="btn">Contact Us</span>
    </nav>
  </header>
  <h1 class="hero-title">Your Partner in Industrial Safety<br>&amp; Compliance</h1>
  <span class="btn" style="left:527px;top:394px;width:146px;height:40px">Contact Us</span>
  <svg class="scroll-badge" viewBox="0 0 98 98" aria-label="Explore and find your dream place">
    <circle cx="49" cy="49" r="47" fill="#fff"/>
    <defs><path id="ring" d="M49,49 m-34,0 a34,34 0 1,1 68,0 a34,34 0 1,1 -68,0"/></defs>
    <text font-family="Montserrat, sans-serif" font-size="9.5" fill="#222" letter-spacing="1"><textPath href="#ring">Explore • and • find • your • Dream • place •</textPath></text>
    <rect x="42" y="38" width="14" height="22" rx="7" fill="none" stroke="#222" stroke-width="1.6"/>
    <line x1="49" y1="43" x2="49" y2="48" stroke="#222" stroke-width="1.6"/>
  </svg>
</section>

<h2 class="section-title" style="top:845px">We are Orvessa</h2>
<p class="about-lead">To provide expert guidance and practical solutions in industrial safety and compliance, delivering clarity, reliability, and peace of mind to every partner we serve.<br><span style="display:block;margin-top:8px">We achieve this mission by staying true to our foundational values:</span></p>

<div class="value left" style="left:104px;top:992px"><h4>Honor</h4><p>Upholding the highest ethical<br>standards.</p></div>
<div class="value left" style="left:104px;top:1078px"><h4>Expertise</h4><p>Leveraging deep industry knowledge<br>to solve complex challenges.</p></div>
<div class="value left" style="left:104px;top:1163px"><h4>Responsibility</h4><p>Taking full accountability from concept<br>through completion.</p></div>

<div class="value-icon" style="left:418px;top:993px"><svg width="26" height="26" viewBox="0 0 26 26" fill="none" stroke="#fff" stroke-width="1.5"><circle cx="13" cy="16" r="7"/><path d="M8 2l5 8 5-8"/></svg></div>
<div class="value-icon" style="left:418px;top:1079px"><svg width="26" height="26" viewBox="0 0 26 26" fill="none" stroke="#fff" stroke-width="1.5"><circle cx="13" cy="13" r="5"/><circle cx="13" cy="13" r="10" stroke-dasharray="3 2"/></svg></div>
<div class="value-icon" style="left:418px;top:1164px"><svg width="26" height="26" viewBox="0 0 26 26" fill="none" stroke="#fff" stroke-width="1.5"><circle cx="9" cy="9" r="4"/><circle cx="17" cy="9" r="4"/><path d="M3 21h20"/></svg></div>

<div class="core-mark" aria-hidden="true"></div>

<div class="value-icon" style="left:735px;top:993px"><svg width="26" height="26" viewBox="0 0 26 26" fill="none" stroke="#fff" stroke-width="1.5"><path d="M6 13l5 5 9-10"/></svg></div>
<div class="value-icon" style="left:735px;top:1079px"><svg width="26" height="26" viewBox="0 0 26 26" fill="none" stroke="#fff" stroke-width="1.5"><rect x="6" y="4" width="14" height="18"/><path d="M9 10h8M9 14h8M9 18h5"/></svg></div>
<div class="value-icon" style="left:735px;top:1164px"><svg width="26" height="26" viewBox="0 0 26 26" fill="none" stroke="#fff" stroke-width="1.5"><path d="M3 13l5-4 5 4 5-4 5 4"/><path d="M8 15l5 4 5-4"/></svg></div>

<div class="value" style="left:800px;top:992px"><h4>Assurance</h4><p>Providing confidence through technically<br>robust solutions.</p></div>
<div class="value" style="left:800px;top:1078px"><h4>Reliability</h4><p>Ensuring consistent performance in demand<br>ing situations.</p></div>
<div class="value" style="left:800px;top:1163px"><h4>Commitment</h4><p>Fulfilling promises and exceeding<br>expectations.</p></div>

<section class="solutions">
  <h2 class="section-title" style="top:46px">Our Solutions</h2>
  <article class="card" style="left:92px">
    <div class="card-icon"><svg width="36" height="36" viewBox="0 0 36 36" fill="none" stroke="#fff" stroke-width="1.6"><circle cx="18" cy="15" r="6"/><circle cx="18" cy="15" r="11" stroke-dasharray="4 3"/><path d="M6 30h24"/></svg></div>
    <h3>Technical Support &amp; Site Services</h3>
    <div class="card-photo" role="img" aria-label="Technician with a headset working at a computer desk in a bright office" style="background:linear-gradient(135deg,#c9d2db,#8796a6 60%,#5b6776)"></div>
  </article>
  <article class="card" style="left:437px">
    <div class="card-icon"><svg width="36" height="36" viewBox="0 0 36 36" fill="none" stroke="#fff" stroke-width="1.6"><circle cx="11" cy="11" r="5"/><path d="M24 14l7 13H17z"/><path d="M24 19v4"/></svg></div>
    <h3 style="width:270px">Risk Management &amp; Compliance Services</h3>
    <div class="card-photo" role="img" aria-label="Business team reviewing charts on a tablet around a meeting table" style="background:linear-gradient(135deg,#3a3d44,#9aa0a6 55%,#e4e4e2)"></div>
  </article>
  <article class="card" style="left:781px">
    <div class="card-icon"><svg width="36" height="36" viewBox="0 0 36 36" fill="none" stroke="#fff" stroke-width="1.6"><circle cx="13" cy="20" r="7"/><circle cx="25" cy="12" r="5"/><circle cx="13" cy="20" r="2.5"/></svg></div>
    <h3 style="width:250px">Transitioning to Fluorine Free Foam</h3>
    <div class="card-photo" role="img" aria-label="Hand holding a translucent piece of foam against a sunset sky" style="background:linear-gradient(160deg,#7d86b8,#d99aa8 50%,#f2b48c)"></div>
  </article>
  <span class="btn" style="left:527px;top:546px;width:146px;height:42px">View More</span>
</section>

<h2 class="section-title" style="top:2073px">Our Work</h2>
<div class="work-slide" style="left:0;width:287px;background:linear-gradient(180deg,#4f4a55,#7a5c4c 55%,#c5762f)" role="img" aria-label="Dam structure lit at dusk beside a river"></div>
<div class="work-slide" style="left:300px;width:601px;background:linear-gradient(135deg,#2f3a48,#6f7f90 50%,#9aa6b2)" role="img" aria-label="Engineers reviewing plans together in a glass office lobby">
  <div class="work-caption">
    <h3>Preserving railways for future generations</h3>
    <p>The first rockfall structure of its type in the UK, with the ability to withstand the impact of a 5-ton boulder falling from 30m</p>
  </div>
</div>
<div class="work-slide" style="left:913px;width:287px;background:linear-gradient(180deg,#3f7fd0,#5b7d48 45%,#4a5a3a 70%,#3b4a44)" role="img" aria-label="Green hillside above a waterfront wall reflected in calm water"></div>

<h2 class="section-title" style="top:2555px">Our&nbsp; People</h2>
<div class="person" style="left:92px"><div class="person-photo" role="img" aria-label="Portrait of a mechanical engineer outdoors" style="background:linear-gradient(180deg,#8a9a6a,#5d6a54)"></div><h4>Maren Holt</h4><p>Mechanical Engineer</p></div>
<div class="person" style="left:350px"><div class="person-photo" role="img" aria-label="Portrait of a project manager against a grey wall" style="background:linear-gradient(180deg,#9a9ea3,#3a4358)"></div><h4>Tobias Reyes</h4><p>Project Manager</p></div>
<div class="person" style="left:609px"><div class="person-photo" role="img" aria-label="Portrait of a structural engineer in an office" style="background:linear-gradient(180deg,#b9a996,#5a5148)"></div><h4>Priya Nandakumar</h4><p>Structural Engineer</p></div>
<div class="person" style="left:865px"><div class="person-photo" role="img" aria-label="Portrait of a sustainability consultant outside a building" style="background:linear-gradient(180deg,#a7abb0,#d8dadc 60%,#7f8790)"></div><h4>Daniel Osei</h4><p>Sustainability Consultant</p></div>
<span class="btn" style="left:527px;top:3026px;width:146px;height:41px">View More</span>

<h2 class="section-title" style="top:3150px">Our&nbsp; People</h2>
<div class="partner" style="left:75px"><span></span></div>
<div class="partner" style="left:287px"><span></span></div>
<div class="partner" style="left:500px"><span></span></div>
<div class="partner" style="left:712px"><span></span></div>
<div class="partner" style="left:925px"><span></span></div>

<footer>
  <div class="footer-main">
    <p class="footer-tagline">We are Orvessa.<br>Your Partner in Industrial.<br>Safety and Compliance</p>
    <nav class="footer-nav"><span>HOME</span>•<span>ABOUT US</span>•<span>SOLUTIONS</span>•<span>CONTACT US</span>•<span>ARTICLES</span></nav>
  </div>
  <div class="footer-base">
    <div class="legal"><span>LEGAL</span><span>|</span><span>COOKIES</span><span>|</span><span>PRIVACY</span></div>
    <div class="footer-brand"><span class="brand-square"></span>ORVESSA</div>
    <div class="footer-company">(C) Orvessa (S) Pte Ltd 2025</div>
    <div class="footer-rule"></div>
    <div class="social">Social</div>
    <div class="copyright">© 2025 ORVESSA. ALL RIGHTS RESERVED.</div>
  </div>
</footer>

</body>
</html>
```